RTV CRAFTED

building services
decks
pergola
renovation
extensions
general building

Target Market(s)

middle to upper class

Industry/Entity Type

building

Contact Information for Business Card

my details 0427839152 pkharlow47@mailvane.net BLD574926

Font styles to use
Serif

Colors
00AB8E
00BBA5
67D7C9
C6EFE9
E9F9F6

Requirements
Must have
• logo on the front and details on the back
Nice to have
• sharp and clean lines

```html
<!DOCTYPE html>
<html lang="en">
<head>
<meta charset="utf-8">
<title>RTV Crafted – Business Card</title>
<link href="https://fonts.googleapis.com/css2?family=Questrial&family=Montserrat:wght@700&display=swap" rel="stylesheet">
<style>
  :root {
    --teal-deep: #00AB8E;
    --teal: #00BBA5;
    --teal-light: #67D7C9;
    --mint: #C6EFE9;
    --mist: #E9F9F6;
    --blush: #E8A0C6;
    --stage: #1DB59F;
  }
  * { margin: 0; padding: 0; box-sizing: border-box; }
  html, body {
    width: 1200px; height: 1200px; overflow: hidden;
    background: var(--stage);
  }
  .canvas { position: relative; width: 1200px; height: 1200px; }
  .card {
    position: absolute; left: 180px; width: 840px; height: 480px;
    border-radius: 40px;
  }
  .card--front {
    top: 71px;
    background: linear-gradient(45deg, #12B9A4 0%, #3DBFAD 45%, #47C3B1 58%, #22B399 80%, #18AE92 100%);
  }
  .card--back { top: 612px; background: var(--mist); }
  .card__line {
    position: absolute; left: 0; width: 100%;
    text-align: center; white-space: nowrap; line-height: 1;
  }
  .name {
    font-family: "Montserrat", Arial, sans-serif; font-weight: 700;
    letter-spacing: 1px;
  }
  .card--front .name { top: 218px; font-size: 44px; color: var(--mist); }
  .card--back .name { top: 145px; font-size: 26px; color: var(--teal-deep); }
  .phone {
    top: 265px; font-family: "Questrial", Arial, sans-serif;
    font-size: 33px; letter-spacing: 1px; color: var(--teal-deep);
  }
  .email {
    top: 306px; font-family: "Questrial", Arial, sans-serif;
    font-size: 15px; letter-spacing: 1px; text-transform: uppercase;
    color: var(--teal-deep);
  }
  .rule { position: absolute; top: 338px; left: 238px; }
  .licence {
    top: 357px; font-family: "Montserrat", Arial, sans-serif; font-weight: 700;
    font-size: 23px; letter-spacing: 1px; color: var(--teal-deep);
  }
</style>
</head>
<body>
<main class="canvas">
  <section class="card card--front">
    <p class="card__line name">RTV CRAFTED</p>
  </section>

  <section class="card card--back">
    <p class="card__line name">RTV CRAFTED</p>
    <p class="card__line phone">0427839152</p>
    <p class="card__line email">pkharlow47@mailvane.net</p>
    <svg class="rule" width="364" height="2" viewBox="0 0 364 2" aria-hidden="true">
      <defs>
        <linearGradient id="ruleFade" x1="0" x2="1" y1="0" y2="0">
          <stop offset="0" stop-color="#E8A0C6" stop-opacity="0"/>
          <stop offset="0.5" stop-color="#E8A0C6" stop-opacity="1"/>
          <stop offset="1" stop-color="#E8A0C6" stop-opacity="0"/>
        </linearGradient>
      </defs>
      <rect width="364" height="2" fill="url(#ruleFade)"/>
    </svg>
    <p class="card__line licence">BLD574926</p>
  </section>
</main>
</body>
</html>
```